Business Card needed for Drainor, a growing Septic Service company

Drainor, a growing local septic service company in Pennsylvania, needs updated business cards. We'd like the business card to feature our logo and communicate that we provide Septic Pumping, Installations/Repairs, Restroom Rentals, and 24/7 Emergency Service. The business card should be eye-catching, bold, and clean/simple. We have been in business almost 10 years and would like to expand and update our business brand and image.

Target Market(s)

Residential and Commercial, New and Current Homeowners

Industry/Entity Type

Service

Contact Information for Business Card

Contact on the business card should be: Dean Harlow Owner & Operator
Phone: 610-555-0187
Email: service@drainor-example.com
Website: www.drainor-example.com
Address: 812 Millbrook Lane Easton PA 18042

Font styles to use
Sans Serif

Colors

Designer to choose colors to be used in the design.

Requirements
Must have
• Feature logo on both side of business card.
Nice to have
• We envision the contact information on one side and our services listed on the other side. Utilize the green from the symbol in our logo as part of the design, overall design color scheme should be white, grey, black.

```html
<!DOCTYPE html>
<html lang="en">
<head>
<meta charset="utf-8">
<title>Drainor Business Card – Front and Back</title>
<link href="https://fonts.googleapis.com/css2?family=Fira+Sans:wght@400;500;700;800&display=swap" rel="stylesheet">
<style>
  :root {
    --band-front: #58585a;
    --band-back: #3a3a3c;
    --card: #ffffff;
    --green: #7ac143;
    --ink: #111111;
    --text: #4a4a4c;
    --divider: #8a8a8c;
    --label: #ffffff;
  }
  * { margin: 0; padding: 0; box-sizing: border-box; }
  html, body { width: 1200px; height: 1200px; overflow: hidden; }
  body { font-family: "Fira Sans", sans-serif; color: var(--text); }

  .band { position: absolute; left: 0; width: 1200px; height: 600px; }
  .band--front { top: 0; background: var(--band-front); }
  .band--back { top: 600px; background: var(--band-back); }
  .band__label {
    position: absolute; left: 23px; top: 20px;
    font-size: 17px; font-weight: 500; color: var(--label); letter-spacing: -0.2px;
  }

  .card {
    position: absolute; left: 240px; top: 84px;
    width: 720px; height: 432px; background: var(--card); overflow: hidden;
  }

  .person { position: absolute; right: 40px; top: 40px; text-align: right; }
  .person__name { font-size: 24px; font-weight: 500; color: var(--green); line-height: 1.15; }
  .person__title { font-size: 17px; color: var(--text); line-height: 1.3; }

  .brand {
    position: absolute; left: 0; right: 0; top: 184px;
    display: flex; align-items: center; justify-content: center; gap: 14px;
  }
  .brand__mark { width: 48px; height: 48px; background: var(--green); }
  .brand__name {
    font-size: 54px; font-weight: 800; color: var(--ink);
    letter-spacing: 1px; text-transform: uppercase; line-height: 1;
  }

  .rule { position: absolute; left: 80px; width: 560px; top: 345px; height: 1px; background: var(--green); }

  .info { position: absolute; top: 360px; font-size: 16px; list-style: none; }
  .info__row { display: flex; align-items: center; height: 29px; white-space: nowrap; }
  .info__icon { width: 16px; height: 16px; margin-right: 8px; flex: none; }
  .info__dot { width: 11px; height: 11px; border-radius: 50%; background: var(--green); margin-right: 9px; flex: none; }
  .info--upper { text-transform: uppercase; }

  .front-left { left: 82px; }
  .front-divider { left: 346px; }
  .front-right { left: 364px; }
  .back-left { left: 105px; }
  .back-divider { left: 354px; }
  .back-right { left: 386px; }

  .divider { position: absolute; top: 367px; width: 1px; height: 44px; background: var(--divider); }
</style>
</head>
<body>

  <section class="band band--front">
    <h2 class="band__label">FRONT SIDE</h2>
    <article class="card card--front">
      <div class="person">
        <div class="person__name">Dean Harlow</div>
        <div class="person__title">Owner &amp; Operator</div>
      </div>

      <div class="brand">
        <span class="brand__mark"></span>
        <span class="brand__name">Drainor</span>
      </div>

      <div class="rule"></div>

      <div class="info front-left">
        <div class="info__row">
          <svg class="info__icon" viewBox="0 0 16 16" fill="var(--green)">
            <path d="M1 6c0-2 3-3 7-3s7 1 7 3v1.5h-3.5V6h-7v1.5H1z"/>
            <path d="M3 8.5h10l1 4.5H2z"/>
            <circle cx="8" cy="10.6" r="1.5" fill="#fff"/>
          </svg>
          <span>610 555 0187</span>
        </div>
        <div class="info__row">
          <svg class="info__icon" viewBox="0 0 16 16" fill="var(--green)">
            <rect x="0.5" y="3" width="15" height="10"/>
            <path d="M1 3.5l7 5 7-5M1 12.5l5-4.5M15 12.5l-5-4.5" stroke="#fff" stroke-width="1.1" fill="none"/>
          </svg>
          <span>service@drainor-example.com</span>
        </div>
      </div>

      <div class="divider front-divider"></div>

      <div class="info front-right">
        <div class="info__row">
          <svg class="info__icon" viewBox="0 0 16 16">
            <circle cx="8" cy="8" r="7.5" fill="var(--green)"/>
            <g stroke="#fff" stroke-width="1" fill="none">
              <ellipse cx="8" cy="8" rx="3" ry="6.5"/>
              <path d="M1.5 8h13M2.5 5h11M2.5 11h11M8 1.5v13"/>
            </g>
          </svg>
          <span>www.drainor-example.com</span>
        </div>
        <div class="info__row">
          <svg class="info__icon" viewBox="0 0 16 16">
            <path d="M8 0.5a6 6 0 0 1 6 6c0 4-6 9-6 9s-6-5-6-9a6 6 0 0 1 6-6z" fill="var(--green)"/>
            <circle cx="8" cy="6.3" r="2.3" fill="#fff"/>
          </svg>
          <span>812 Millbrook Lane Easton PA 18042</span>
        </div>
      </div>
    </article>
  </section>

  <section class="band band--back">
    <h2 class="band__label">BACK SIDE</h2>
    <article class="card card--back">
      <div class="brand">
        <span class="brand__mark"></span>
        <span class="brand__name">Drainor</span>
      </div>

      <div class="rule"></div>

      <ul class="info info--upper back-left">
        <li class="info__row"><span class="info__dot"></span>Septic Pumping,</li>
        <li class="info__row"><span class="info__dot"></span>Installations/Repairs</li>
      </ul>

      <div class="divider back-divider"></div>

      <ul class="info info--upper back-right">
        <li class="info__row"><span class="info__dot"></span>Restroom Rentals,</li>
        <li class="info__row"><span class="info__dot"></span>24/7 Emergency Service</li>
      </ul>
    </article>
  </section>

</body>
</html>
```